COMMERCIAL REAL ESTATE FLYER TEMPLATE

We need a template flyer designed that we can use for a current commercial real estate listing and subsequently use as a template for future listings. We have uploaded images and files to provide an example of an older flyer template we have used. If you have questions or would like to discuss, please contact us at Wade@TLMVX.net. Colors selected should be in line with our attached business card and logo design. Output should be 8.5" X 11".

Target Market(s)

Commercial Real Estate. NO RESIDENTIAL. Needs to have a professional commercial presentation with no reference to residential real estate.

Industry/Entity Type

Real Estate Agent

Font styles to use
Serif

Colors

Designer to choose colors to be used in the design.

Requirements
Must have
• MUST BE SAVED AND ADJUSTABLE IN ONE OF THE FOLLOWING FORMATES: MICROSOFT POWERPOINT, PUBLISHER OR WORD. THIS IS IMPORTANT SO OUR TEAM CAN EASILLY UPDATE TEMPLATE IN READILLY AVAILABLE PROGRAMS THAT ARE SIMPLE FOR TEAM MEMBERS TO USE.
Nice to have
• Needs to have first page template with header and footer displaying our logo, address, phone, email address and contact information for the listing agent. There need to be placeholders that can be easily adjusted based on specific listings. Placeholders will be used for pictures or aerials as the case requires. Needs to have a second page that has header and footer with a clean open block in the middle of the page so agents can customize with site specific details.
Should not have
• There should be no reference to residential. We are a commercial real estate organization that does not do any residential.

```html
<!DOCTYPE html>
<html lang="en">
<head>
<meta charset="utf-8">
<title>Flex Industrial Listing Flyer</title>
<link href="https://fonts.googleapis.com/css2?family=Roboto:ital,wght@0,400;0,500;0,700;0,900;1,700;1,900&display=swap" rel="stylesheet">
<style>
  :root {
    --brand-red: #c1272d;
    --card-red-top: #ec3a43;
    --card-red-bottom: #b51c25;
    --accent-yellow: #fff200;
    --page-bg: #ebebeb;
    --outer-bg: #ffffff;
    --ink-grey: #4a4a4a;
    --white: #ffffff;
  }
  * { box-sizing: border-box; margin: 0; padding: 0; }
  html, body { width: 1200px; height: 1200px; overflow: hidden; background: var(--outer-bg); }
  body { font-family: "Roboto", Arial, sans-serif; }
  .canvas { position: relative; width: 1200px; height: 1200px; }
  .backdrop { position: absolute; left: 90px; top: 0; width: 1004px; height: 1200px; background: var(--page-bg); }
  .flyer { position: absolute; left: 147px; top: 24px; width: 890px; height: 1152px; background: var(--white); box-shadow: 0 4px 18px rgba(0,0,0,0.18); overflow: hidden; }
  .abs { position: absolute; }

  /* header */
  .hero-photo { left: 0; top: 0; width: 890px; height: 486px;
    background: radial-gradient(ellipse at 55% 55%, #9a7a55 0%, #7c6a52 35%, #5d5347 70%, #3f3a35 100%); }
  .brand-block { left: 35px; top: 35px; width: 187px; height: 153px; background: var(--brand-red);
    display: flex; flex-direction: column; align-items: center; justify-content: center; color: var(--white); font-weight: 700; }
  .brand-block .brand-name { font-size: 34px; letter-spacing: 2px; line-height: 1; }
  .brand-block .brand-sub { font-size: 10.5px; letter-spacing: 0.4px; margin-top: 10px; }

  .contact-panel { left: 355px; top: 35px; width: 535px; height: 153px; background: rgba(255,255,255,0.78);
    border-radius: 48px 0 0 0; }
  .agent-name { left: 390px; top: 86px; font-size: 22px; font-weight: 700; color: var(--brand-red); }
  .agent-title { left: 390px; top: 116px; font-size: 14px; color: var(--ink-grey); }
  .panel-divider { width: 1px; height: 96px; background: var(--brand-red); top: 74px; }
  .info-head { font-size: 8.5px; font-weight: 700; color: var(--brand-red); text-decoration: underline; }
  .info-line { font-size: 7.8px; font-weight: 700; color: #333; line-height: 13.5px; }

  .title-band { left: 35px; top: 223px; width: 820px; height: 229px; background: rgba(70,68,66,0.5); }
  .listing-title { left: 92px; top: 246px; font-size: 41px; font-weight: 900; color: var(--accent-yellow); letter-spacing: -0.3px; white-space: nowrap; }
  .status-pill { left: 94px; top: 307px; width: 236px; height: 38px; background: var(--accent-yellow); border-radius: 10px;
    color: var(--brand-red); font-style: italic; font-weight: 900; font-size: 20px; display: flex; align-items: center; justify-content: center; }
  .address-marker { left: 35px; top: 363px; width: 40px; height: 60px; background: var(--accent-yellow); }
  .listing-address { left: 94px; top: 357px; font-size: 24px; color: var(--white); line-height: 42px; }

  /* gallery */
  .gallery { left: 0; top: 0; width: 890px; height: 1152px; pointer-events: none; }
  .gallery-shadow { left: 140px; top: 935px; width: 230px; height: 30px; border-radius: 50%;
    background: radial-gradient(ellipse, rgba(0,0,0,0.22), rgba(0,0,0,0) 70%); }

  /* feature card */
  .feature-card { left: 510px; top: 522px; width: 345px; height: 424px; border-radius: 10px;
    background: linear-gradient(160deg, var(--card-red-top), var(--card-red-bottom)); box-shadow: 0 2px 8px rgba(0,0,0,0.15); }
  .feature-frame { left: 528px; top: 540px; width: 309px; height: 388px; border: 1.5px solid var(--white); border-radius: 10px; }
  .feature-heading { left: 582px; top: 617px; font-size: 21px; font-weight: 700; color: var(--white); text-decoration: underline; text-underline-offset: 3px; }
  .feature-list { left: 582px; top: 652px; list-style: none; }
  .feature-list li { display: flex; align-items: center; height: 22.7px; font-size: 8.6px; font-weight: 700; color: var(--white); }
  .feature-list svg { width: 10px; height: 10px; margin-right: 7px; flex: none; }

  /* footer */
  .footer-photo { left: 0; top: 986px; width: 890px; height: 166px;
    background: linear-gradient(90deg, #a03038, #b8424a 40%, #c45a5e 70%, #b8474d); }
  .footer-brand { left: 35px; top: 1022px; width: 114px; height: 93px; background: var(--brand-red);
    display: flex; flex-direction: column; align-items: center; justify-content: center; color: var(--white); font-weight: 700; box-shadow: 0 1px 4px rgba(0,0,0,0.2); }
  .footer-brand .brand-name { font-size: 21px; letter-spacing: 1.5px; line-height: 1; }
  .footer-brand .brand-sub { font-size: 6.5px; margin-top: 7px; }
  .footer-contact { left: 201px; top: 1019px; font-size: 14px; color: var(--white); line-height: 20px; }
  .disclaimer { left: 446px; top: 1024px; width: 409px; height: 91px; background: rgba(255,255,255,0.1);
    padding: 7px 9px; font-size: 7px; line-height: 12.2px; color: var(--white); text-align: justify; }
</style>
</head>
<body>
<div class="canvas">
  <div class="backdrop"></div>
  <div class="flyer">
    <div class="abs hero-photo" role="img" aria-label="Photo of the private office interior with wooden desk and armchairs"></div>

    <div class="abs brand-block">
      <span class="brand-name">TLMVX</span>
      <span class="brand-sub">COMMERCIAL REAL ESTATE</span>
    </div>

    <div class="abs contact-panel"></div>
    <div class="abs agent-name">Wade S. Tolliver</div>
    <div class="abs agent-title">President &nbsp;|&nbsp; CEO</div>
    <div class="abs panel-divider" style="left:586px"></div>
    <div class="abs" style="left:604px; top:78px">
      <div class="info-head">Address</div>
      <div class="info-line" style="margin-top:6px">P.O. Box 240517<br>The Woodlands, TX 77393</div>
    </div>
    <div class="abs panel-divider" style="left:729px"></div>
    <div class="abs" style="left:746px; top:78px">
      <div class="info-head">Contact</div>
      <div class="info-line" style="margin-top:6px">Direct: 281.555.0143<br>Fax: 281.555.0187<br>Email: wade@tlmvx.net<br>Website: www.tlmvx.net</div>
    </div>

    <div class="abs title-band"></div>
    <div class="abs listing-title">FLEX INDUSTRIAL, HOUSTON TEXAS</div>
    <div class="abs status-pill">FOR SALE OR LEASE</div>
    <div class="abs address-marker"></div>
    <div class="abs listing-address">20815 Ridgeway Park Dr., Houston,<br>Texas 77073</div>

    <div class="abs gallery-shadow"></div>
    <svg class="abs gallery" viewBox="0 0 890 1152" aria-hidden="false">
      <defs>
        <linearGradient id="kitchen" x1="0" y1="0" x2="0" y2="1">
          <stop offset="0" stop-color="#c9b98f"/><stop offset="0.5" stop-color="#b9854e"/><stop offset="1" stop-color="#cbb99a"/>
        </linearGradient>
        <linearGradient id="office" x1="0" y1="0" x2="1" y2="1">
          <stop offset="0" stop-color="#cfc6a8"/><stop offset="0.6" stop-color="#7a4a2c"/><stop offset="1" stop-color="#c8b796"/>
        </linearGradient>
        <linearGradient id="workstation" x1="0" y1="0" x2="0" y2="1">
          <stop offset="0" stop-color="#a39877"/><stop offset="0.5" stop-color="#8e8870"/><stop offset="1" stop-color="#d0c4a6"/>
        </linearGradient>
      </defs>
      <polygon role="img" aria-label="Photo of the break room kitchen with wooden cabinets" points="140.5,530 246,590 246,702 140.5,758 36,702 36,590" fill="url(#kitchen)" stroke="var(--brand-red)" stroke-width="4"/>
      <polygon role="img" aria-label="Photo of a private office with desk and bookcase" points="371,530 476,590 476,702 371,758 266,702 266,590" fill="url(#office)" stroke="var(--brand-red)" stroke-width="4"/>
      <polygon role="img" aria-label="Photo of a workstation with computer and chair" points="256,716 361,774 361,886 256,942 151,886 151,774" fill="url(#workstation)" stroke="var(--brand-red)" stroke-width="4"/>
    </svg>

    <div class="abs feature-card"></div>
    <div class="abs feature-frame"></div>
    <div class="abs feature-heading">FLEX INDUSTRIAL</div>
    <ul class="abs feature-list">
      <li><svg viewBox="0 0 10 10"><circle cx="5" cy="5" r="4.2" fill="none" stroke="#fff" stroke-width="1.2"/><path d="M2.8 5h4M5.2 3.2 7 5 5.2 6.8" fill="none" stroke="#fff" stroke-width="1.2"/></svg>Well Maintained Owner-Occupied Building</li>
      <li><svg viewBox="0 0 10 10"><circle cx="5" cy="5" r="4.2" fill="none" stroke="#fff" stroke-width="1.2"/><path d="M2.8 5h4M5.2 3.2 7 5 5.2 6.8" fill="none" stroke="#fff" stroke-width="1.2"/></svg>Great Location Near IAH &amp; The Woodlands</li>
      <li><svg viewBox="0 0 10 10"><circle cx="5" cy="5" r="4.2" fill="none" stroke="#fff" stroke-width="1.2"/><path d="M2.8 5h4M5.2 3.2 7 5 5.2 6.8" fill="none" stroke="#fff" stroke-width="1.2"/></svg>Easy Access to Hardy, IH-45 &amp; Beltway 8</li>
      <li><svg viewBox="0 0 10 10"><circle cx="5" cy="5" r="4.2" fill="none" stroke="#fff" stroke-width="1.2"/><path d="M2.8 5h4M5.2 3.2 7 5 5.2 6.8" fill="none" stroke="#fff" stroke-width="1.2"/></svg>Building Area: 11,820 SF (HCAD)</li>
      <li><svg viewBox="0 0 10 10"><circle cx="5" cy="5" r="4.2" fill="none" stroke="#fff" stroke-width="1.2"/><path d="M2.8 5h4M5.2 3.2 7 5 5.2 6.8" fill="none" stroke="#fff" stroke-width="1.2"/></svg>Land Area: 41,616 SF (HCAD)</li>
      <li><svg viewBox="0 0 10 10"><circle cx="5" cy="5" r="4.2" fill="none" stroke="#fff" stroke-width="1.2"/><path d="M2.8 5h4M5.2 3.2 7 5 5.2 6.8" fill="none" stroke="#fff" stroke-width="1.2"/></svg>Office Build-Out: Approx. 2,820 SF (Owner)</li>
      <li><svg viewBox="0 0 10 10"><circle cx="5" cy="5" r="4.2" fill="none" stroke="#fff" stroke-width="1.2"/><path d="M2.8 5h4M5.2 3.2 7 5 5.2 6.8" fill="none" stroke="#fff" stroke-width="1.2"/></svg>Loading: Three (3) Grade-Level</li>
      <li><svg viewBox="0 0 10 10"><circle cx="5" cy="5" r="4.2" fill="none" stroke="#fff" stroke-width="1.2"/><path d="M2.8 5h4M5.2 3.2 7 5 5.2 6.8" fill="none" stroke="#fff" stroke-width="1.2"/></svg>Eave Height: Approx. 22'</li>
      <li><svg viewBox="0 0 10 10"><circle cx="5" cy="5" r="4.2" fill="none" stroke="#fff" stroke-width="1.2"/><path d="M2.8 5h4M5.2 3.2 7 5 5.2 6.8" fill="none" stroke="#fff" stroke-width="1.2"/></svg>Outside Storage: Room To Add Fenced Yard</li>
    </ul>

    <div class="abs footer-photo" role="img" aria-label="Red-tinted photo of the office interior"></div>
    <div class="abs footer-brand">
      <span class="brand-name">TLMVX</span>
      <span class="brand-sub">COMMERCIAL REAL ESTATE</span>
    </div>
    <div class="abs footer-contact">
      Wade S. Tolliver<br>President | CEO<br>Phone: (281) 555-0142<br>E-Mail: wade@tlmvx.net<br>TREC Broker License: 9004871
    </div>
    <div class="abs disclaimer">
      The information contained herein has, we believe, been obtained from reliable sources, and we have no reason to doubt the accuracy thereof. All such information is submitted, subject to errors, omissions or changes in condition prior to sale, lease or withdrawal without notice. All information contained herein should be verified by the person relying thereon. We have not made and will not make any warranty or representation as to the condition of the property nor the presence of any hazardous substances or any environmental or other conditions that may affect the value or suitability of the property.
    </div>
  </div>
</div>
</body>
</html>
```